Manuka honey jar label for new Manuka brand

We are planning to start a Manuka honey brand and we need to design the label for the honey jar. Manuka honey is an up and coming product and the market is still young in our country.
Our market is dominated by 1 brand: Orvana Health (photo attached). To the people who know what Manuka honey is, they associate it with Orvana Health in the same way people associate Cola with Zindle Pop or printer copies with Quorvix.
The good news is that a lot of people do not know yet what Manuka honey is and we still have the opportunity of being the first brand they get to know. At the same time, we still need to be able to take at least a bite out of the Orvana Health market share.
The Orvana Health label for their jar I think is not just absolutely gorgeous but it also does its job extremely well. It only features 3 informations:
- name of brand/logo (Orvana Health)
- name of product (Manuka Honey)
- and mgo rating which is like a rating of how strong the honey is
By having just this information on a relatively small label, their label SCREAMS Manuka by having the Manuka words twice (the brand and the product name) and people develop this association between Orvana Health and Manuka products in general.
Our product will also be in a similar square plastic jar. It will also be dark tinted, that´s important to note. We can also go for a blue cap but in order to differentiate ourselves from Orvana Health we thought of maybe choosing a black lid instead. I uploaded 2 jars, 1 with black lid and 1 with gold (although it looks more like mustard) that you can use for simulations. They are pretty accurate of the type of jars and lids that we can have.
The label has total length of about 20cm. One side of the jar has 5,5 cm of the label and the height of the label is 4,5 cm. We can also use selective gold laminating on the label but we cannot have custom shape label at this point as Orvana Health does with its tree logo that sticks outside the label.
I need the design for the entire label but the focus should be on the front part, that is the part that sells and catches your eye. Like Orvana Health, the front part I want to have 3 vital informations:
- name of brand/logo (in our case Velmora Botanica) - we do not have a pre-existing logo, this needs to be created alongside the label
- and mgo rating
As "other" information we also need the net weight "250 g" alongside with the typical "e" to appear on the front. That is a legal requirement.
Optionally, you can add a small phrase somewhere like "Harvested in New Zealand" or "Made in New Zealand" since this is a product that is only made there and in some areas of Australia.
This is pretty much all the info. As a final note, there are a ton of beautiful premium Manuka honey jar labels. But they are too fancy and when you look at them you don´t instantly recognize that it is Manuka Honey.
This instant recognition is vital! With this small jar there is the danger for customers to think that maybe it´s medicine, maybe it´s sports supplements etc. This is a relatively small product and imagine you just glance on it on the retail shelf. Instantly you must think it is Manuka Honey and that it is beautiful. And if you see it on the shelf next to Orvana Health, it would be best to also think that you would rather buy this (it gives you more trust) than the Orvana Health.
One final note: I do not want the bee as an insect on the label. I think some people are turned off when they see an insect with its small legs and make a bad association that there are insects inside. I do not mind symbolism or somehow super stylized bee in a modern way, but I do not want a plain insect on the label.
For any other questions, I am at your disposal. Thank you very much for taking the time to send us a proposal!

```html
<!DOCTYPE html>
<html lang="en">
<head>
<meta charset="utf-8">
<title>Velmora Botanica – Manuka Honey Label</title>
<link href="https://fonts.googleapis.com/css2?family=Marcellus&family=Playfair+Display:wght@700;800&family=Barlow:wght@500;600;700&display=swap" rel="stylesheet">
<style>
  :root {
    --canvas: #ffffff;
    --label-black: #1d1b1b;
    --label-black-soft: #2c2a2a;
    --gold: #cfae62;
    --gold-deep: #b8923f;
    --gold-tag: #d9bc72;
    --paper: #ffffff;
    --ink: #2e2e2e;
    --ink-soft: #4a4a4a;
    --mgo-red: #c5504f;
    --weight-red: #a3262d;
  }
  * { margin: 0; padding: 0; box-sizing: border-box; }
  html, body {
    width: 1200px; height: 1200px; overflow: hidden;
    background: var(--canvas);
  }
  .label {
    position: absolute; left: 120px; top: 210px;
    width: 960px; height: 780px;
    background: var(--paper);
    overflow: hidden;
  }
  .label__brand-panel {
    position: absolute; left: 0; top: 0; width: 100%; height: 390px;
    background: linear-gradient(180deg, var(--label-black-soft) 0%, var(--label-black) 70%);
  }
  .brand-name {
    position: absolute; left: 0; width: 100%; top: 70px;
    text-align: center;
    font-family: "Marcellus", serif;
    font-size: 104px; line-height: 108px;
    color: var(--gold);
    letter-spacing: 1px;
  }
  .label__divider {
    position: absolute; left: 0; top: 386px; width: 100%; height: 7px;
    background: var(--gold-deep);
  }
  .origin-tag {
    position: absolute; left: 50%; top: 360px;
    transform: translateX(-50%);
    width: 540px; height: 60px;
    background: var(--gold-tag);
    display: flex; align-items: center; justify-content: center;
    font-family: "Barlow", sans-serif; font-weight: 600;
    font-size: 36px; letter-spacing: 1px;
    color: var(--ink);
  }
  .product-name {
    position: absolute; left: 0; width: 100%; top: 455px;
    text-align: center;
    font-family: "Playfair Display", serif; font-weight: 800;
    font-size: 76px; line-height: 90px;
    color: var(--ink);
    letter-spacing: 0.5px;
  }
  .spec {
    position: absolute; top: 590px;
    font-family: "Barlow", sans-serif;
    text-align: center;
  }
  .spec--mgo { left: 140px; width: 170px; }
  .spec--weight { right: 130px; width: 200px; }
  .spec__label {
    display: block;
    font-weight: 500; font-size: 34px; line-height: 40px;
    color: var(--ink-soft);
  }
  .spec__value {
    display: block;
    margin-top: 12px; padding-bottom: 8px;
    font-weight: 700; font-size: 48px; line-height: 54px;
    border-bottom: 4px dotted var(--ink-soft);
  }
  .spec--mgo .spec__value { color: var(--mgo-red); }
  .spec--weight .spec__value { color: var(--weight-red); }
  .estimated-mark { font-weight: 600; font-size: 40px; margin-left: 6px; }
  .emblem {
    position: absolute; left: 50%; top: 625px;
    transform: translateX(-50%);
    width: 170px; height: 105px;
    border-radius: 50px;
    background: radial-gradient(ellipse at center, var(--gold) 0%, var(--gold-tag) 60%, rgba(217,188,114,0.35) 100%);
  }
</style>
</head>
<body>
  <main class="label">
    <section class="label__brand-panel">
      <h1 class="brand-name">velmora<br>botanica</h1>
    </section>
    <div class="label__divider"></div>
    <div class="origin-tag">MADE IN NEW ZEALAND</div>

    <h2 class="product-name">MANUKA HONEY</h2>

    <div class="spec spec--mgo">
      <span class="spec__label">MGO</span>
      <span class="spec__value">450+</span>
    </div>

    <div class="emblem" role="img" aria-label="Gold stylised bee emblem flanked by two small flower sprigs"></div>

    <div class="spec spec--weight">
      <span class="spec__label">NET.WT.</span>
      <span class="spec__value">250g<span class="estimated-mark">e</span></span>
    </div>
  </main>
</body>
</html>
```